Independent theatre company and venue needs funky web design

Web design for theatre company based in Brisbane Australia. Innovative, grassroots theatre space needs to promote shows in quirky industrial venue. Design needs to be funky, arty but website feels solid and business savvy as well. We need a portal for selling tickets online.
Lamp and Ladder is the production company behind this project. We also create theatre in fresh, intimate and humanistic ways.
Target Market(s)
ages 20s-80s
Interested in the arts and fresh, quirky local experiences
Requirements
Must have
- Pages:
- Performances (What's on)
- Hire the Venue (info and enquiry form)
- About Lamp and Ladder (history and profile)
- Buy Tickets (patrons can purchase tickets to the shows on at the venue)
- Contact Us/Subscribe
Nice to have
- http://www.brickyard27stage.com/
- Similar in content to this one
- Ideally a website I can update shows (so wordpress or similar user friendly)

```html
<!DOCTYPE html>
<html lang="en">
<head>
<meta charset="utf-8">
<title>Lamp and Ladder – Independent Theatre</title>
<link rel="stylesheet" href="https://fonts.googleapis.com/css2?family=Lobster&family=Open+Sans:ital,wght@0,400;0,600;1,400&display=swap">
<style>
  :root {
    --backdrop: #bdbdbd;
    --page: #ffffff;
    --ink: #111111;
    --text: #444444;
    --muted: #666666;
    --welcome-bg: #ebebeb;
    --rule: #c9c9c9;
    --footer-bg: #333333;
    --footer-text: #e6e6e6;
    --footer-muted: #bdbdbd;
    --bottom-bar: #101010;
    --hero-dark: #1c1c1c;
    --hero-mid: #6e6e6e;
  }
  * { box-sizing: border-box; margin: 0; padding: 0; }
  html, body { width: 1037px; height: 1200px; overflow: hidden; }
  body {
    background: var(--backdrop);
    font-family: "Open Sans", Arial, sans-serif;
    color: var(--text);
  }
  .page {
    position: absolute; left: 139px; top: 0;
    width: 758px; height: 1200px;
    background: var(--page);
    box-shadow: 0 0 12px rgba(0,0,0,.25);
  }
  /* header */
  .site-header { position: relative; height: 90px; }
  .brand {
    position: absolute; left: 20px; top: 26px;
    display: flex; align-items: center; gap: 8px;
    font-family: "Lobster", cursive; font-size: 27px; color: var(--ink);
  }
  .brand-dot { width: 22px; height: 22px; border-radius: 50%; background: var(--ink); }
  .social-top { position: absolute; right: 20px; top: 16px; display: flex; gap: 5px; }
  .social-top span { width: 22px; height: 22px; border-radius: 50%; background: var(--ink); }
  .main-nav {
    position: absolute; right: 20px; top: 55px;
    display: flex; gap: 14px;
    font-style: italic; font-size: 11px; color: #333;
  }
  .main-nav .sep { color: #666; font-style: normal; }
  .main-nav .active { text-decoration: underline; color: var(--ink); }
  /* hero */
  .hero {
    position: relative; height: 335px;
    background: radial-gradient(ellipse at 50% 40%, var(--hero-mid) 0%, #3a3a3a 45%, var(--hero-dark) 100%);
  }
  .hero-caption {
    position: absolute; left: 0; right: 0; bottom: 0; height: 56px;
    background: rgba(0,0,0,.72);
    display: flex; align-items: center; justify-content: center;
    font-family: "Lobster", cursive; font-size: 30px; color: #fff;
  }
  /* welcome */
  .welcome {
    position: relative; height: 232px; background: var(--welcome-bg);
    text-align: center; overflow: hidden;
  }
  .welcome-decor {
    position: absolute; left: 505px; top: 4px; width: 230px; height: 230px;
    border-radius: 50%;
    background: radial-gradient(circle, rgba(0,0,0,.09) 0%, rgba(0,0,0,0) 70%);
  }
  .section-title {
    position: relative; display: flex; align-items: center; justify-content: center; gap: 45px;
    padding-top: 34px;
    font-family: "Lobster", cursive; font-size: 22px; color: #222;
  }
  .section-title::before, .section-title::after {
    content: ""; width: 90px; height: 1px; background: var(--rule); margin-top: 4px;
  }
  .welcome p {
    position: relative; margin: 18px auto 0; width: 690px;
    font-size: 10.2px; line-height: 15.6px; color: var(--text);
  }
  .more-btn {
    position: relative; display: inline-flex; align-items: center; justify-content: center;
    margin-top: 17px; width: 45px; height: 45px; border-radius: 50%;
    background: var(--ink); color: #fff; font-size: 10px;
  }
  /* performances */
  .performances { height: 345px; padding-top: 49px; }
  .show-grid { display: flex; gap: 11px; padding: 0 20px; }
  .show-card { width: 171px; text-align: center; }
  .show-image { height: 117px; }
  .show-image.red { background: linear-gradient(180deg, #1d1a33 0%, #5a3a4a 55%, #8a6f7e 100%); }
  .show-image.grey1 { background: linear-gradient(180deg, #9a9a9a 0%, #4a4a4a 100%); }
  .show-image.grey2 { background: linear-gradient(180deg, #2a2a2a 0%, #555 60%, #222 100%); }
  .show-image.grey3 { background: linear-gradient(180deg, #3a3a3a 0%, #777 50%, #2b2b2b 100%); }
  .show-title {
    font-family: "Lobster", cursive; font-size: 15.5px; line-height: 18.5px; color: #222;
    padding: 8px 0 7px; border-bottom: 1px solid var(--rule);
  }
  .show-dates { font-size: 9.5px; color: var(--text); padding: 6px 0 7px; border-bottom: 1px solid var(--rule); }
  .perf-actions { display: flex; justify-content: center; gap: 12px; margin-top: 33px; }
  .btn-dark {
    width: 123px; height: 27px; background: var(--ink); color: #fff;
    font-size: 9px; display: flex; align-items: center; justify-content: center;
  }
  /* footer */
  .site-footer { position: relative; height: 168px; background: var(--footer-bg); color: var(--footer-text); }
  .footer-col { position: absolute; top: 30px; }
  .footer-heading { font-family: "Lobster", cursive; font-size: 16px; color: #fff; margin-bottom: 12px; }
  .col-venue { left: 22px; }
  .col-venue .address { font-size: 10px; line-height: 12.5px; }
  .col-venue .hours { font-size: 9px; line-height: 11.5px; color: var(--footer-muted); margin-top: 12px; }
  .col-find { left: 251px; padding-left: 0; }
  .divider { position: absolute; top: 34px; width: 1px; height: 100px; background: #4a4a4a; }
  .social-foot { display: flex; gap: 10px; margin-left: 8px; }
  .social-foot span { width: 12px; height: 12px; background: #fff; }
  .col-news { left: 411px; }
  .news-fields { display: flex; gap: 14px; }
  .field {
    width: 153px; height: 28px; border: 1px solid #888; color: #ccc;
    font-size: 8.5px; display: flex; align-items: center; padding-left: 8px;
  }
  .signup-btn {
    margin-top: 17px; width: 68px; height: 25px; background: #fff; color: #222;
    font-size: 11px; display: flex; align-items: center; justify-content: center;
  }
  .bottom-bar {
    height: 30px; background: var(--bottom-bar); color: #8a8a8a;
    font-size: 8px; display: flex; align-items: center; justify-content: center; gap: 14px;
  }
  .bottom-bar .terms { text-decoration: underline; color: #aaa; }
</style>
</head>
<body>
<div class="page">
  <header class="site-header">
    <div class="brand"><span class="brand-dot"></span>Lamp and Ladder</div>
    <div class="social-top" aria-label="Social links"><span></span><span></span><span></span></div>
    <nav class="main-nav">
      <span class="active">Performances</span><span class="sep">-</span>
      <span>Hire the Venue</span><span class="sep">-</span>
      <span>About Lamp and Ladder</span><span class="sep">-</span>
      <span>Buy Tickets</span><span class="sep">-</span>
      <span>Contact Us</span>
    </nav>
  </header>

  <section class="hero" role="img" aria-label="Black and white photo of dancers leaping mid-air on stage">
    <div class="hero-caption">Transforming Is Just The Beginning</div>
  </section>

  <section class="welcome">
    <div class="welcome-decor" role="img" aria-label="Faint theatre masks decoration"></div>
    <h2 class="section-title">Welcome</h2>
    <p>Lorem ipsum dolor sit amet, consectetur adipiscing elit, sed do eiusmod tempor incididunt ut labore et dolore magna aliqua. Ut enim ad minim veniam, quis nostrud exercitation ullamco laboris nisi ut aliquip ex ea commodo consequat. Duis aute irure dolor in reprehenderit in voluptate velit esse cillum dolore eu fugiat nulla pariatur. Excepteur sint occaecat cupidatat non proident, sunt in culpa qui officia deserunt mollit anim id est laborum.</p>
    <span class="more-btn">more</span>
  </section>

  <section class="performances">
    <div class="show-grid">
      <article class="show-card">
        <div class="show-image red" role="img" aria-label="Stage photo of a performer in red standing over kneeling cast"></div>
        <h3 class="show-title">Lorem Ipsum is simply<br>dummy text</h3>
        <div class="show-dates">8th Feb - 25th Feb</div>
      </article>
      <article class="show-card">
        <div class="show-image grey1" role="img" aria-label="Silhouettes of figures behind a window"></div>
        <h3 class="show-title">Lorem Ipsum is simply<br>dummy text</h3>
        <div class="show-dates">8th Feb - 25th Feb</div>
      </article>
      <article class="show-card">
        <div class="show-image grey2" role="img" aria-label="Black and white photo of a seated performer in a hat"></div>
        <h3 class="show-title">Lorem Ipsum is simply<br>dummy text</h3>
        <div class="show-dates">8th Feb - 25th Feb</div>
      </article>
      <article class="show-card">
        <div class="show-image grey3" role="img" aria-label="Black and white portrait of a seated performer"></div>
        <h3 class="show-title">Lorem Ipsum is simply<br>dummy text</h3>
        <div class="show-dates">8th Feb - 25th Feb</div>
      </article>
    </div>
    <div class="perf-actions">
      <span class="btn-dark">ALL PERFORMANCES</span>
      <span class="btn-dark">BUY TICKETS</span>
    </div>
  </section>

  <footer class="site-footer">
    <div class="footer-col col-venue">
      <h4 class="footer-heading">Lamp and Ladder</h4>
      <div class="address">18 Carrow Lane<br>Marlow QLD 4101</div>
      <div class="hours">Open during show seasons only :<br>Tuesday – Saturday 8pm</div>
    </div>
    <div class="divider" style="left:211px"></div>
    <div class="footer-col col-find">
      <h4 class="footer-heading">Find Us On</h4>
      <div class="social-foot"><span></span><span></span><span></span></div>
    </div>
    <div class="divider" style="left:366px"></div>
    <div class="footer-col col-news">
      <h4 class="footer-heading">Signup For Newsletter</h4>
      <div class="news-fields">
        <div class="field">Name ...</div>
        <div class="field">Email ...</div>
      </div>
      <div class="signup-btn">SIGNUP</div>
    </div>
  </footer>
  <div class="bottom-bar">
    <span>COPYRIGHT © LAMP AND LADDER 2015-2016. ALL RIGHT RESERVED.</span>
    <span>|</span>
    <span class="terms">TERMS &amp; CONDITIONS</span>
  </div>
</div>
</body>
</html>
```